Flyer Template Design

I have attached 4 files. I would like a design template that could be used across these documents so that they have a common look and feel. The content of the documents is tested and should not be changed significantly. The images can be changed. I have also attache our logo for color compatibility.
Updates

Need extra days to review

Target Market(s)

Wealthy Christian donors

Font styles to use
Serif
Sans Serif

```html
<!DOCTYPE html>
<html lang="en">
<head>
<meta charset="utf-8">
<title>God's Heart for the Nations – The Harvest Fund</title>
<link href="https://fonts.googleapis.com/css2?family=Cinzel:wght@600&family=Tinos:ital,wght@0,400;1,700&family=Open+Sans:ital,wght@1,300;1,400&display=swap" rel="stylesheet">
<style>
  :root {
    --sky: #1ba8e0;
    --sky-band: #5fc8ef;
    --leaf: #8cc963;
    --leaf-line: #c6e3a6;
    --ink: #222;
    --band-ink: #1b2b33;
    --placeholder: #e7e8e9;
    --placeholder-inner: #eeeeee;
    --placeholder-text: #3a3a3a;
  }
  * { margin: 0; padding: 0; box-sizing: border-box; }
  html, body { width: 848px; height: 1200px; overflow: hidden; background: #fff; }
  .flyer { position: relative; width: 848px; height: 1200px; color: var(--ink);
    font-family: "Tinos", "Times New Roman", serif; font-size: 15px; line-height: 18.6px; }

  .brand { position: absolute; right: 45px; top: 86px; display: flex; align-items: center; gap: 10px; }
  .brand-mark { width: 26px; height: 26px; background: var(--sky); }
  .brand-name { font-family: "Tinos", serif; font-size: 24px; line-height: 28px; color: var(--sky); }

  .section-title { position: absolute; left: 77px; font-family: "Cinzel", serif; font-weight: 600;
    font-size: 30px; line-height: 32px; color: var(--sky); letter-spacing: -0.2px; }
  .title-nations { top: 164px; }
  .title-task { top: 720px; }

  .intro { position: absolute; left: 77px; top: 205px; width: 682px; }
  .intro p { margin-bottom: 18.6px; }
  .book { font-weight: 700; font-style: italic; }

  .column { position: absolute; left: 77px; width: 389px; text-align: justify; }
  .column p { margin-bottom: 18.6px; }
  .column-scripture { top: 435px; }
  .column-task { top: 759px; }

  .photo { position: absolute; left: 484px; width: 297px; background: var(--placeholder);
    display: flex; align-items: center; justify-content: center;
    font-family: "Tinos", serif; font-size: 36px; color: var(--placeholder-text); }
  .photo-one { top: 437px; height: 238px; }
  .photo-two { top: 756px; height: 141px; }
  .photo .inner { background: var(--placeholder-inner);
    display: flex; align-items: center; justify-content: center; }
  .photo-one .inner { width: 205px; height: 187px; }
  .photo-two .inner { width: 147px; height: 141px; }

  .tagline { position: absolute; left: 77px; width: 694px; top: 938px; display: flex; align-items: center; gap: 10px;
    font-family: "Open Sans", sans-serif; font-style: italic; font-weight: 400; font-size: 18px; color: var(--ink); }
  .tagline::before, .tagline::after { content: ""; flex: 1; height: 1px; }
  .tagline::before { background: var(--sky-band); opacity: .5; }
  .tagline::after { background: var(--leaf-line); }

  .appeal { position: absolute; left: 90px; width: 668px; top: 975px; text-align: center; }

  .band { position: absolute; left: 67px; width: 714px; height: 40px; border-radius: 10px;
    display: flex; align-items: center; justify-content: center;
    font-family: "Open Sans", sans-serif; font-style: italic; font-weight: 300; font-size: 23px; color: var(--band-ink); }
  .band-join { top: 1061px; background: var(--sky-band); }
  .band-contact { top: 1111px; background: var(--leaf); }
</style>
</head>
<body>
<main class="flyer">
  <header class="brand">
    <span class="brand-mark" aria-hidden="true"></span>
    <span class="brand-name">The Harvest Fund</span>
  </header>

  <h1 class="section-title title-nations">GOD’S HEART FOR THE NATIONS</h1>

  <section class="intro">
    <p>From beginning to end, the Bible reveals God’s heart for “the nations.”</p>
    <p>In <span class="book">Genesis,</span> God promises Abraham, “through your offspring all nations on the earth will be blessed.”</p>
    <p>The <span class="book">Psalms</span> prophesy that “all the nations you have made will come and worship before you, Lord…”</p>
    <p>In <span class="book">Isaiah,</span> God promises the Messiah, “I will make you a light to the nations, that my salvation may reach to the ends of the earth.”</p>
    <p><span class="book">Daniel</span> sees “one like a son of man” who “was given authority, glory and sovereign power; all nations and peoples of every language worshiped him.”</p>
  </section>

  <section class="column column-scripture">
    <p>In <span class="book">Matthew,</span> Jesus commands his apostles to “Go and make disciples of all nations.” And he links his return to the completion of that task, saying, “This gospel of the kingdom will be preached in the whole world as a testimony to all nations, and then the end will come.”</p>
    <p>In <span class="book">Revelation,</span> John sees a “great multitude that no one could number, from every nation, from all tribes and peoples and languages, standing before the throne…” In the Bible, the word “nations” refers to people groups: groups of people who share a common ethnicity, culture, and language. Amazingly, there are more than 12,000 of these nations scattered around the world—and God has promised that every one of them will be included in His Kingdom.</p>
  </section>
  <div class="photo photo-one" role="img" aria-label="Photo placeholder: people from the nations"><div class="inner">Photos</div></div>

  <h2 class="section-title title-task">FINISHING THE TASK</h2>
  <section class="column column-task">
    <p>Today, there are still 500 nations who are not yet represented in God’s Kingdom. No one has ever proclaimed the gospel to these “unengaged” people groups, and there are no believers among them. For these groups, God’s promises have yet to be fulfilled. Most of these groups are small and located in remote, difficult places. But because we now know who and where they are, by God’s grace it is possible that we can engage every one of them with the gospel within the next 3 years.</p>
  </section>
  <div class="photo photo-two" role="img" aria-label="Photo placeholder: missionaries in the field"><div class="inner">Photos</div></div>

  <p class="tagline">You can make that happen.</p>
  <p class="appeal">Partner with the Harvest Fund and finance the missionaries who are taking the gospel for the first time to those last remaining people groups. Your investment will “hasten the coming of the day of God” by accelerating the effort to make “disciples in every nation.” In 2018, our partners helped take the gospel to 231 people groups in 35 countries.</p>

  <div class="band band-join">Join us as we invest to make disciples in “all nations” by 2022.</div>
  <div class="band band-contact">To learn more, email Daniel Reeve at dreeve@harvestfund.org.</div>
</main>
</body>
</html>
```